Redesign and programming website interior design

Calvora is an interior design company that operates in the private and public sectors.
The website www.calvora-example.ch already exists. Now we want to change some elements and add some things. In addition, new images will be added. IMPORTANT: The page should appear calm and elegant.
!!IMPORTANT: THE PAGE MUST BE PROGRAMMED IN THE DIVI-BUILDER!!

```html
<!DOCTYPE html>
<html lang="en">
<head>
<meta charset="utf-8">
<title>Calvora – Interior Design</title>
<link href="https://fonts.googleapis.com/css2?family=Noto+Serif:wght@400;500;600;700&display=swap" rel="stylesheet">
<style>
:root{
  --ink:#1c1c28;
  --accent:#f7a21b;
  --band:#ececef;
  --footer:#1f2430;
  --white:#ffffff;
  --muted:#6b6b78;
}
*{margin:0;padding:0;box-sizing:border-box}
html,body{width:1200px;height:3968px;overflow:hidden;background:var(--white)}
body{position:relative;font-family:"Noto Serif",Georgia,serif;color:var(--ink)}
.abs{position:absolute}
.brand{display:flex;align-items:center;gap:10px;font-size:22px;font-weight:500;letter-spacing:1px;color:var(--ink)}
.brand .dot{width:16px;height:16px;border-radius:50%;background:currentColor}
.nav a{position:absolute;top:145px;font-size:18px;font-weight:700;color:var(--ink);text-decoration:none}
.nav a.active{color:var(--accent)}
.btn-outline{left:986px;top:136px;width:174px;height:40px;border:2px solid var(--accent);display:flex;align-items:center;justify-content:center;font-weight:700;font-size:18px}
.photo{position:absolute}
.hero-title{left:40px;top:302px;font-size:39px;font-weight:700}
.hero-sub{left:40px;top:364px;font-size:29px;font-weight:600}
.hero-text{left:40px;top:414px;width:440px;font-size:18px;line-height:25px}
.partners{left:40px;top:596px;width:1120px;height:117px;background:var(--band);display:flex;justify-content:space-around;align-items:center}
.partner{display:flex;align-items:center;gap:8px;font-size:24px;font-weight:500;color:#2b2b36}
.partner i{width:20px;height:20px;border-radius:50%;background:#2b2b36;display:block}
.section-title{width:1200px;text-align:center;font-size:39px;font-weight:600}
.about-text{left:608px;top:884px;width:550px;font-size:28px;line-height:37px}
.read-more{left:608px;top:1214px;display:flex;align-items:center;gap:9px;color:var(--accent);font-weight:700;font-size:18px}
.read-more span{width:22px;height:22px;border-radius:50%;background:var(--accent)}
.btn-fill{left:513px;top:2404px;width:174px;height:54px;background:var(--accent);color:var(--white);display:flex;align-items:center;justify-content:center;font-size:18px;font-weight:700;box-shadow:0 3px 6px rgba(0,0,0,.15)}
.underline{left:476px;top:2601px;width:40px;height:3px;background:var(--ink)}
.card{position:absolute;top:2643px;width:364px;height:355px;padding:38px 22px}
.card.raised{background:var(--white);box-shadow:0 4px 18px rgba(0,0,0,.12)}
.card .head{display:flex;gap:14px;align-items:flex-start}
.avatar{width:40px;height:40px;border-radius:50%;background:#9fb6c8}
.name{font-size:19px;font-weight:700;color:#2d3a5a}
.stars{display:flex;gap:8px;margin-top:6px}
.stars svg{width:16px;height:16px;fill:var(--accent)}
.quote{margin-top:30px;font-size:18px;font-weight:700;line-height:24.6px}
.dots{left:527px;top:3038px;display:flex;gap:12px}
.dots span{width:40px;height:13px;border-radius:7px;border:2px solid var(--accent)}
.dots span.on{background:var(--accent)}
.map{left:0;top:3129px;width:1200px;height:476px;background:linear-gradient(135deg,#eceff2,#e2e7ea 60%,#eef0e8)}
.footer{left:0;top:3605px;width:1200px;height:363px;background:var(--footer);color:var(--white)}
.fcol{position:absolute;top:98px;font-size:28px;line-height:45px}
.fcol h3{font-size:29px;font-weight:600;margin-bottom:4px}
.social{display:flex;gap:18px;margin-top:8px}
.social span{width:32px;height:32px;border-radius:50%;background:var(--white)}
.legal{position:absolute;top:326px;font-size:18px;font-weight:500}
.copy{left:40px;display:flex;align-items:center;gap:20px}
.copy span{width:28px;height:28px;border-radius:50%;background:var(--white);color:var(--footer);font-size:15px;font-weight:700;display:flex;align-items:center;justify-content:center}
</style>
</head>
<body>

<header>
  <div class="abs brand" style="left:58px;top:141px"><span class="dot"></span>CALVORA</div>
  <nav class="nav">
    <a class="active" style="left:465px">Home</a>
    <a style="left:560px">About</a>
    <a style="left:657px">Projects</a>
  </nav>
  <div class="abs btn-outline">Contact</div>
</header>

<section class="hero">
  <h1 class="abs hero-title">Modern Fyrnitures</h1>
  <h2 class="abs hero-sub">with best quality and best price</h2>
  <p class="abs hero-text">With us by your side, interiors, dining rooms, offices and gardens are not just functional, but places of luxury. Contact us for a non-binding appointment and let us put your vision into action.</p>
  <div class="photo" role="img" aria-label="Dining room with glass wall overlooking the sea at dusk" style="left:513px;top:226px;width:647px;height:328px;background:linear-gradient(180deg,#b7b3b9 0%,#8e96a6 45%,#4d5665 70%,#2c2a2c 100%)"></div>
</section>

<div class="abs partners">
  <div class="partner"><i></i>orbita</div>
  <div class="partner"><i></i>celda</div>
  <div class="partner"><i></i>veranto</div>
  <div class="partner"><i></i>Lumio</div>
  <div class="partner"><i></i>petalo</div>
  <div class="partner"><i></i>kyro</div>
</div>

<section class="about">
  <h2 class="abs section-title" style="top:792px">About</h2>
  <div class="photo" role="img" aria-label="Bright living room with sofas and glass doors to a terrace" style="left:40px;top:887px;width:551px;height:351px;background:linear-gradient(180deg,#d8d8d6 0%,#b9bdb2 45%,#8a8678 75%,#5c5650 100%)"></div>
  <p class="abs about-text">Teodor is the head-chef here.He is extremely experienced and he is someone who can catch the vibe of people,the type of food to serve and he always makes sure that food is upto the mark and "No halfway house in the quality of food you serve" is his main motto,says our head-ched Teodor</p>
  <div class="abs read-more"><span></span>Read More</div>
</section>

<section class="works">
  <h2 class="abs section-title" style="top:1318px">Our Works</h2>
  <div class="photo" role="img" aria-label="Dark lounge with pendant lamp, white brick wall and tufted sofa" style="left:40px;top:1407px;width:614px;height:955px;background:linear-gradient(160deg,#6f5b45 0%,#8a8c8e 35%,#b7b5b0 60%,#3a302a 100%)"></div>
  <div class="photo" role="img" aria-label="White desk with computer, coffee maker and blossom branches" style="left:684px;top:1407px;width:476px;height:475px;background:linear-gradient(180deg,#f1f0ee 0%,#e4e2df 60%,#cfccc7 100%)"></div>
  <div class="photo" role="img" aria-label="Sunny dining corner with round white table and pampas grass" style="left:684px;top:1890px;width:476px;height:472px;background:linear-gradient(180deg,#e9e5df 0%,#d8d1c6 60%,#b29a76 100%)"></div>
  <div class="abs btn-fill">View All</div>
</section>

<section class="testimonials">
  <h2 class="abs section-title" style="top:2552px;left:-13px">Testimonial</h2>
  <div class="abs underline"></div>

  <article class="card" style="left:40px">
    <div class="head"><span class="avatar"></span><div><div class="name">Lena Marsh</div>
      <div class="stars"><svg viewBox="0 0 10 10"><path d="M5 0l1.5 3.3 3.5.4-2.6 2.4.7 3.5L5 7.8 1.9 9.6l.7-3.5L0 3.7l3.5-.4z"/></svg><svg viewBox="0 0 10 10"><path d="M5 0l1.5 3.3 3.5.4-2.6 2.4.7 3.5L5 7.8 1.9 9.6l.7-3.5L0 3.7l3.5-.4z"/></svg><svg viewBox="0 0 10 10"><path d="M5 0l1.5 3.3 3.5.4-2.6 2.4.7 3.5L5 7.8 1.9 9.6l.7-3.5L0 3.7l3.5-.4z"/></svg><svg viewBox="0 0 10 10"><path d="M5 0l1.5 3.3 3.5.4-2.6 2.4.7 3.5L5 7.8 1.9 9.6l.7-3.5L0 3.7l3.5-.4z"/></svg><svg viewBox="0 0 10 10"><path d="M5 0l1.5 3.3 3.5.4-2.6 2.4.7 3.5L5 7.8 1.9 9.6l.7-3.5L0 3.7l3.5-.4z"/></svg></div></div></div>
    <p class="quote">"Whether you're totally new at social ads or have some level of knowledge, Mirela is great at gauging where you're at and taking things from there. It's easy to keep up, and you'll definitely want to get in more time with someone as accomplished as her."</p>
  </article>

  <article class="card raised" style="left:417px">
    <div class="head"><span class="avatar"></span><div><div class="name">Selin Vardar</div>
      <div class="stars"><svg viewBox="0 0 10 10"><path d="M5 0l1.5 3.3 3.5.4-2.6 2.4.7 3.5L5 7.8 1.9 9.6l.7-3.5L0 3.7l3.5-.4z"/></svg><svg viewBox="0 0 10 10"><path d="M5 0l1.5 3.3 3.5.4-2.6 2.4.7 3.5L5 7.8 1.9 9.6l.7-3.5L0 3.7l3.5-.4z"/></svg><svg viewBox="0 0 10 10"><path d="M5 0l1.5 3.3 3.5.4-2.6 2.4.7 3.5L5 7.8 1.9 9.6l.7-3.5L0 3.7l3.5-.4z"/></svg><svg viewBox="0 0 10 10"><path d="M5 0l1.5 3.3 3.5.4-2.6 2.4.7 3.5L5 7.8 1.9 9.6l.7-3.5L0 3.7l3.5-.4z"/></svg><svg viewBox="0 0 10 10"><path d="M5 0l1.5 3.3 3.5.4-2.6 2.4.7 3.5L5 7.8 1.9 9.6l.7-3.5L0 3.7l3.5-.4z"/></svg></div></div></div>
    <p class="quote">"Whether you're totally new at social ads or have some level of knowledge, Mirela is great at gauging where you're at and taking things from there. It's easy to keep up, and you'll definitely want to get in more time with someone as accomplished as her."</p>
  </article>

  <article class="card" style="left:797px">
    <div class="head"><span class="avatar"></span><div><div class="name">Omar Reval</div>
      <div class="stars"><svg viewBox="0 0 10 10"><path d="M5 0l1.5 3.3 3.5.4-2.6 2.4.7 3.5L5 7.8 1.9 9.6l.7-3.5L0 3.7l3.5-.4z"/></svg><svg viewBox="0 0 10 10"><path d="M5 0l1.5 3.3 3.5.4-2.6 2.4.7 3.5L5 7.8 1.9 9.6l.7-3.5L0 3.7l3.5-.4z"/></svg><svg viewBox="0 0 10 10"><path d="M5 0l1.5 3.3 3.5.4-2.6 2.4.7 3.5L5 7.8 1.9 9.6l.7-3.5L0 3.7l3.5-.4z"/></svg><svg viewBox="0 0 10 10"><path d="M5 0l1.5 3.3 3.5.4-2.6 2.4.7 3.5L5 7.8 1.9 9.6l.7-3.5L0 3.7l3.5-.4z"/></svg><svg viewBox="0 0 10 10"><path d="M5 0l1.5 3.3 3.5.4-2.6 2.4.7 3.5L5 7.8 1.9 9.6l.7-3.5L0 3.7l3.5-.4z"/></svg></div></div></div>
    <p class="quote">“The links to high-value blog posts already make the book worth it, never mind the amazing insight and context provided by Dorian. Must buy for #FreshBuilders looking to break in or senior engineers looking to grow!”</p>
  </article>

  <div class="abs dots"><span></span><span class="on"></span><span></span></div>
</section>

<div class="abs map" role="img" aria-label="Street map of the studio's neighbourhood"></div>

<footer class="abs footer">
  <div class="abs brand" style="left:58px;top:180px;color:var(--white)"><span class="dot"></span>CALVORA</div>
  <div class="fcol" style="left:297px"><h3>Pages</h3>Home<br>About<br>Projects</div>
  <div class="fcol" style="left:608px"><h3>Address</h3>Lindenweg 14<br>8570 Talwil</div>
  <div class="fcol" style="left:919px"><h3>Contacts</h3>+41 70 555 01 23<br>mail@calvora.ch
    <div class="social"><span></span><span></span><span></span><span></span></div>
  </div>
  <div class="legal copy"><span>C</span>All Copyright Reserved To CALVORA</div>
  <div class="legal" style="left:815px">Privacy</div>
  <div class="legal" style="left:917px">Terms &amp; Condition</div>
  <div class="legal" style="left:1122px">FAQ</div>
</footer>

</body>
</html>
```